2016 Ledgerline Summit Postcard Design

The Ledgerline Summit. A Summit For Account Chasers...By Account Chasers.
The Ledgerline Summit was created to provide quality content at a reasonable price-point to allow organizations to send multiple attendees and encourage active participation. This event is intended for debt collection professionals who are:

Senior Level Executives
Front Line Collection Managers
Compliance Professionals
Trainers
While there are many great conferences within our industry to choose from, most collection conferences just scratch the surface when attempting to provide real world solutions. The Ledgerline Summit was created to provide debt collection professionals with a foundation of direction, insight, and actionable solutions that can be applied regardless of the size of an organization. Join us at the inaugural Ledgerline Summit as we assemble an expert team of operations, compliance, and training professionals that will deep dive into real world solutions for today’s real world debt collection issues. Here is what you can expect:

Solution driven sessions, not sponsor driven sessions
Substance from "In The Trenches" experts who live it, breathe it, work it...every day
Learn operational, compliance, and training strategies that have proven success
Understand how to efficiently and effectively manage YOUR resources
Apply state of the art technology solutions

Target Market(s)

Debt collection agencies and creditors

Industry/Entity Type

Financial Service

Font styles to use
Serif

Requirements
Must have
• link to website www.LLS2016.example and use of image provided LLSCover. Use same color scheme as the LLSCover image

```html
<!DOCTYPE html>
<html lang="en">
<head>
<meta charset="utf-8">
<title>2016 Ledgerline Summit Postcard</title>
<link rel="stylesheet" href="https://fonts.googleapis.com/css2?family=Bebas+Neue&family=Lato:ital,wght@0,400;0,700;1,700&family=Arimo:wght@400;700&display=swap">
<style>
  :root {
    --page: #e7e4df;
    --ink: #1b1b1b;
    --yellow: #f3ee4a;
    --yellow-pale: #f5f6b4;
    --blue: #1aaecb;
    --teal: #2aa9bd;
    --white: #ffffff;
    --rule: #8a8a8a;
  }
  html, body {
    margin: 0;
    width: 907px;
    height: 1200px;
    overflow: hidden;
    background: var(--page);
  }
  .card {
    position: absolute;
    left: 102px;
    width: 698px;
    display: block;
  }
  .card--front { top: 62px; height: 500px; }
  .card--back { top: 635px; height: 505px; }

  .headline { font-family: "Bebas Neue", sans-serif; }
  .headline--name { fill: var(--yellow); font-size: 64px; }
  .headline--sub { fill: var(--yellow); font-size: 56px; }
  .headline--year { fill: var(--white); font-size: 104px; }
  .tagline { font-family: "Arimo", sans-serif; font-weight: 700; font-size: 17px; fill: var(--white); }
  .band-label { font-family: "Lato", sans-serif; font-size: 17px; fill: var(--ink); }
  .band-label--lg { font-weight: 700; font-size: 21px; }
  .band-label--sm { font-size: 14px; }
  .event-place { font-family: "Arimo", sans-serif; font-weight: 700; font-size: 21px; fill: var(--yellow); }
  .event-date { font-family: "Arimo", sans-serif; font-weight: 700; font-size: 20px; fill: var(--white); }
  .event-time { font-family: "Arimo", sans-serif; font-weight: 700; font-size: 22px; fill: var(--yellow); }
  .web-note { font-family: "Lato", sans-serif; font-size: 13px; fill: var(--yellow); }
  .web-url { font-family: "Arimo", sans-serif; font-size: 20px; fill: var(--white); }
  .brand-name { font-family: "Lato", sans-serif; font-weight: 700; font-size: 14px; fill: var(--teal); letter-spacing: 1px; }
  .about-copy { font-family: "Lato", sans-serif; font-size: 12.3px; fill: var(--white); }
  .audience-intro { font-family: "Lato", sans-serif; font-style: italic; font-weight: 700; font-size: 16px; fill: var(--yellow); }
  .audience-item { font-family: "Lato", sans-serif; font-weight: 700; font-size: 13px; fill: var(--white); }
</style>
</head>
<body>

<svg class="card card--front" viewBox="0 0 698 500" xmlns="http://www.w3.org/2000/svg">
  <defs>
    <linearGradient id="skyline-tone" x1="0" y1="0" x2="0" y2="1">
      <stop offset="0" stop-color="#4a4a4a"/>
      <stop offset="0.42" stop-color="#8c8c8c"/>
      <stop offset="0.5" stop-color="#3a3a3a"/>
      <stop offset="1" stop-color="#2b2b2b"/>
    </linearGradient>
  </defs>
  <rect class="cover-photo" width="698" height="500" fill="url(#skyline-tone)" role="img" aria-label="Black and white photo of a city riverfront skyline with a tall arch at dusk"/>
  <polygon class="panel-dark" points="0,0 198,0 365,228 300,500 0,500" fill="var(--ink)" fill-opacity="0.88"/>
  <polygon class="chevron-stripe" points="198,0 236,0 388,228 330,500 300,500 365,228" fill="var(--yellow)" fill-opacity="0.55"/>
  <polygon class="footer-dark" points="403,418 698,418 698,500 403,500" fill="var(--ink)" fill-opacity="0.85"/>

  <text class="headline headline--name" x="22" y="122">LEDGERLINE</text>
  <text class="headline headline--sub" x="22" y="192">SUMMIT</text>
  <text class="headline headline--year" x="22" y="300">2016</text>
  <text class="tagline" x="24" y="338">A Summit For Account Chasers...</text>
  <text class="tagline" x="24" y="360">By Account Chasers</text>

  <text class="brand-name" x="400" y="395">LEDGERLINE</text>

  <polygon class="band band--yellow" points="0,385 325,385 343,418 0,418" fill="var(--yellow)"/>
  <text class="band-label" x="22" y="408">Event Location and Date</text>
  <polygon class="band band--blue" points="0,418 375,418 403,500 0,500" fill="var(--blue)"/>
  <text class="event-place" x="22" y="446">SAINT LOUIS, MISSOURI</text>
  <text class="event-date" x="22" y="476">MARCH 21,2016 - MARCH 23,2016</text>

  <text class="web-note" x="684" y="444" text-anchor="end">Visit our website for more information</text>
  <text class="web-url" x="668" y="473" text-anchor="end">www.LLS2016.example</text>
  <g class="icon-globe" transform="translate(683,466)" fill="none" stroke="var(--white)" stroke-width="1.3">
    <circle r="6"/><ellipse rx="2.6" ry="6"/><line x1="-6" y1="0" x2="6" y2="0"/>
  </g>
</svg>

<svg class="card card--back" viewBox="0 0 698 505" xmlns="http://www.w3.org/2000/svg">
  <defs>
    <clipPath id="back-panel">
      <polygon points="0,0 285,0 395,235 330,505 0,505"/>
    </clipPath>
    <linearGradient id="skyline-faint" x1="0" y1="0" x2="0" y2="1">
      <stop offset="0" stop-color="#1e1e1e"/>
      <stop offset="0.5" stop-color="#3d3d3d"/>
      <stop offset="0.6" stop-color="#262626"/>
      <stop offset="1" stop-color="#1e1e1e"/>
    </linearGradient>
  </defs>
  <rect class="back-blank" width="698" height="505" fill="var(--white)"/>
  <g clip-path="url(#back-panel)">
    <rect width="698" height="505" fill="var(--ink)"/>
    <rect class="cover-photo" y="40" width="400" height="280" fill="url(#skyline-faint)" role="img" aria-label="Faint city riverfront skyline with a tall arch"/>
  </g>
  <polygon class="chevron-stripe" points="285,0 318,0 428,235 335,505 300,505 395,235" fill="var(--yellow-pale)"/>
  <rect class="footer-dark" x="0" y="440" width="410" height="65" fill="var(--ink)"/>

  <polygon class="band band--yellow" points="0,25 185,25 198,47 0,47" fill="var(--yellow)"/>
  <text class="band-label band-label--sm" x="20" y="41">About Ledgerline Summit</text>

  <text class="about-copy" x="20" y="64">The Ledgerline Summit was created to provide</text>
  <text class="about-copy" x="20" y="80">quality content at a reasonable price-point to allow</text>
  <text class="about-copy" x="20" y="96">organizations to send multiple attendees and</text>
  <text class="about-copy" x="20" y="112">encourage active participation.</text>

  <text class="audience-intro" x="20" y="140">This event is intended for debt collection</text>
  <text class="audience-intro" x="20" y="161">professionals who are:</text>

  <g class="audience-list" fill="var(--yellow)">
    <circle cx="25" cy="192" r="3.5"/>
    <circle cx="25" cy="216" r="3.5"/>
    <circle cx="25" cy="241" r="3.5"/>
    <circle cx="25" cy="266" r="3.5"/>
  </g>
  <text class="audience-item" x="51" y="197">Senior Level Executives</text>
  <text class="audience-item" x="51" y="221">Front Line Collection Managers</text>
  <text class="audience-item" x="51" y="246">Compliance Professionals</text>
  <text class="audience-item" x="51" y="271">Trainers</text>

  <polygon class="band band--yellow" points="0,313 268,313 285,347 0,347" fill="var(--yellow)"/>
  <text class="band-label band-label--lg" x="20" y="337">Event Details</text>
  <polygon class="band band--blue" points="0,347 300,347 330,440 0,440" fill="var(--blue)"/>
  <text class="event-place" x="17" y="376" style="font-size:19px">SAINT LOUIS, MISSOURI</text>
  <text class="event-date" x="17" y="398" style="font-size:17px">MARCH 21,2016 - MARCH 23,2016</text>
  <text class="event-time" x="17" y="429">8:00 AM - 12:00 PM</text>

  <text class="web-note" x="17" y="457" style="font-size:14px">Visit our website for more information</text>
  <g class="icon-globe" transform="translate(25,475)" fill="none" stroke="var(--white)" stroke-width="1.3">
    <circle r="6"/><ellipse rx="2.6" ry="6"/><line x1="-6" y1="0" x2="6" y2="0"/>
  </g>
  <text class="web-url" x="40" y="483" style="font-size:22px">www.LLS2016.example</text>

  <text class="brand-name" x="382" y="390">LEDGERLINE</text>

  <rect class="stamp-box" x="596" y="45" width="72" height="80" fill="none" stroke="var(--rule)" stroke-width="1"/>
  <g class="address-lines" stroke="var(--rule)" stroke-width="1">
    <line x1="470" y1="233" x2="675" y2="233"/>
    <line x1="470" y1="270" x2="675" y2="270"/>
    <line x1="470" y1="308" x2="675" y2="308"/>
  </g>
</svg>

</body>
</html>
```